Design uplift of Quillamber.com site

The site needs to be fast and responsive down to mobile.
Needs to use the supplied Video as the homepage background.
Needs to use Generate Press as the theme - Site theme to be a child theme of Generate Press.
Needs to have a button above the fold for an offer of a free email course on how to set up a medical software project.
Needs to use the Quillamber logo. This logo has been trademarked.

The existing site is at: www.quillamber.com

```html
<!DOCTYPE html>
<html lang="en">
<head>
<meta charset="utf-8">
<title>Quillamber</title>
<link href="https://fonts.googleapis.com/css2?family=Jost:wght@400;500;600&display=swap" rel="stylesheet">
<style>
:root{
  --blue:#3aaee8;
  --blue-dark:#1d92d6;
  --ink:#231d1a;
  --page:#f4f4f4;
  --white:#ffffff;
  --text:#333333;
  --muted:#666666;
  --line:#dddddd;
}
*{margin:0;padding:0;box-sizing:border-box}
html,body{width:1200px;height:3839px;overflow:hidden}
body{background:var(--page);font-family:'Jost',sans-serif;color:var(--text);position:relative}
.abs{position:absolute}
.btn{position:absolute;display:flex;align-items:center;justify-content:center;border-radius:20px;font-size:13px;color:var(--white)}
.btn-blue{background:linear-gradient(180deg,#4cc0f2,var(--blue-dark))}
.btn-dark{background:var(--ink)}

.site-header{position:absolute;left:0;top:0;width:1200px;height:124px;background:var(--white)}
.brand{position:absolute;display:flex;align-items:center;gap:12px;font-weight:600;font-size:40px;color:var(--ink)}
.brand-dot{width:52px;height:52px;border-radius:50%;background:var(--blue)}
.main-nav a{position:absolute;top:80px;font-size:13px;color:var(--text);text-decoration:none}
.main-nav a.active{color:var(--blue)}
.main-nav a.active::after{content:"";position:absolute;left:0;right:0;bottom:-6px;height:2px;background:var(--blue)}

.hero{position:absolute;left:0;top:124px;width:1200px;height:740px}

.intro-title{position:absolute;left:0;width:1200px;top:898px;text-align:center;font-size:30px;font-weight:500;line-height:37px;color:var(--ink)}

.about-photo{position:absolute;left:146px;top:1060px;width:408px;height:408px;border-radius:50%;background:radial-gradient(circle at 55% 40%,#e8e4df,#b9b2aa 70%,#8f877f)}
.about-title{position:absolute;left:622px;top:1143px;font-size:33px;font-weight:500;color:var(--ink)}
.about-rule{position:absolute;left:622px;top:1196px;width:71px;height:3px;background:#999}
.about-text{position:absolute;left:624px;top:1233px;width:420px;font-size:13px;line-height:22px;color:var(--text)}

.services{position:absolute;left:0;top:1460px;width:1200px;height:820px}
.services-title{position:absolute;left:500px;top:1627px;font-size:32px;font-weight:500;color:var(--white)}
.service-name{position:absolute;left:113px;top:1766px;font-size:33px;line-height:40px;font-weight:500;color:var(--white)}
.service-rule{position:absolute;left:113px;top:1870px;width:114px;height:4px;background:var(--blue)}
.service-text{position:absolute;left:113px;width:390px;font-size:12.5px;line-height:22px;color:var(--white)}
.photo{position:absolute}
.dots{position:absolute;background-image:radial-gradient(circle,#6b6360 1px,transparent 1.4px);background-size:6px 6px}

.blog-title{position:absolute;left:0;width:1200px;top:2326px;text-align:center;font-size:33px;font-weight:500;color:var(--ink)}
.post{position:absolute;top:2386px;width:333px;height:430px;background:var(--page);border:1px solid var(--line)}
.post.featured{box-shadow:0 4px 12px rgba(0,0,0,.18);background:var(--page)}
.post-photo{position:absolute;left:10px;top:10px;width:311px;height:222px}
.post-date{position:absolute;left:136px;top:202px;width:60px;height:60px;border-radius:50%;background:var(--blue);border:3px solid var(--white);color:var(--white);font-size:14px;line-height:16px;text-align:center;padding-top:11px}
.post-heading{position:absolute;left:0;right:0;top:276px;text-align:center;font-size:15px;font-weight:500;color:var(--ink)}
.post-excerpt{position:absolute;left:38px;right:38px;top:308px;text-align:center;font-size:13.5px;line-height:16px;color:var(--muted)}
.post-arrow{position:absolute;left:142px;bottom:0;width:49px;height:26px;background:var(--blue);border-radius:12px 12px 0 0;display:flex;align-items:center;justify-content:center}

.contact-title{position:absolute;left:0;width:1200px;top:2955px;text-align:center;font-size:33px;font-weight:500;color:var(--ink)}
.field{position:absolute;background:var(--white);font-size:12px;color:var(--muted);padding:14px 16px}

.site-footer{position:absolute;left:0;top:3340px;width:1200px;height:430px}
.footer-head{position:absolute;top:3514px;font-size:16px;font-weight:500;color:var(--white)}
.footer-rule{position:absolute;top:3548px;width:60px;height:2px;background:var(--blue)}
.quick-links{position:absolute;left:428px;top:3568px;list-style:none;font-size:12.5px;line-height:22.5px;color:var(--white)}
.quick-links li::before{content:">";margin-right:8px}
.contact-line{position:absolute;left:604px;display:flex;gap:10px;font-size:13px;line-height:15px;color:var(--white)}
.contact-line svg{flex:none;margin-top:1px}
.bottom-bar{position:absolute;left:0;top:3770px;width:1200px;height:69px;background:var(--page)}
.copyright{position:absolute;left:75px;top:3793px;font-size:12px;color:var(--text)}
.social{position:absolute;top:3784px;width:34px;height:34px;border-radius:50%}
</style>
</head>
<body>

<header class="site-header">
  <div class="brand" style="left:75px;top:36px"><span class="brand-dot"></span>Quillamber</div>
  <div class="btn btn-blue" style="left:900px;top:30px;width:107px;height:34px">Login</div>
  <div class="btn btn-dark" style="left:1016px;top:30px;width:108px;height:34px">Register</div>
  <nav class="main-nav">
    <a class="active" style="left:624px">Home</a>
    <a style="left:709px">About us</a>
    <a style="left:811px">Our Services</a>
    <a style="left:940px">Blog</a>
    <a style="left:1015px">Contact us</a>
    <svg style="position:absolute;left:1110px;top:80px" width="20" height="20" viewBox="0 0 20 20"><circle cx="8" cy="8" r="6" fill="none" stroke="#888" stroke-width="1.6"/><line x1="12.5" y1="12.5" x2="18" y2="18" stroke="#888" stroke-width="1.6"/></svg>
  </nav>
</header>

<section class="hero">
  <svg width="1200" height="740" viewBox="0 0 1200 740">
    <defs>
      <linearGradient id="heroTone" x1="0" y1="0" x2="1" y2="1">
        <stop offset="0" stop-color="#1c3a6b"/>
        <stop offset=".5" stop-color="#3e6ea8"/>
        <stop offset="1" stop-color="#0e1c38"/>
      </linearGradient>
    </defs>
    <rect role="img" aria-label="Video background: robotic surgery in a blue-lit operating room" width="1200" height="740" fill="url(#heroTone)"/>
    <polygon points="0,736 1200,606 1200,740 0,740" fill="var(--page)"/>
    <polygon points="0,733 1200,604 1200,612 0,741" fill="var(--white)"/>
    <polygon points="596,677 1200,612 1200,736" fill="var(--blue)"/>
    <circle cx="599" cy="371" r="26" fill="none" stroke="#fff" stroke-width="3"/>
    <polygon points="592,358 592,384 612,371" fill="none" stroke="#fff" stroke-width="3" stroke-linejoin="round"/>
    <rect x="220" y="436" width="97" height="33" rx="16" fill="var(--blue)"/>
  </svg>
</section>

<h1 class="intro-title">How Could You Enlighten<br>Your Business?</h1>
<div class="btn btn-dark" style="left:504px;top:997px;width:174px;height:36px">Free Email Course</div>

<div class="about-photo" role="img" aria-label="Doctor working on a laptop at her desk"></div>
<h2 class="about-title">About us</h2>
<div class="about-rule"></div>
<p class="about-text">Quillamber' mission is to provide a custom software development service across a range of technologies by using best practice agile methodologies and tools to deliver customer value on time and within budget.</p>
<div class="btn btn-blue" style="left:628px;top:1346px;width:153px;height:38px">Read More</div>

<section class="services">
  <svg width="1200" height="820" viewBox="0 0 1200 820"><polygon points="0,142 1200,8 1200,676 0,808" fill="var(--ink)"/></svg>
</section>
<h2 class="services-title">Our Service</h2>
<div class="photo" role="img" aria-label="Doctor with stethoscope viewing a holographic body scan" style="left:723px;top:1575px;width:365px;height:338px;background:linear-gradient(135deg,#cfe3f2,#4a8fc8 55%,#163a6e)"></div>
<div class="dots" style="left:662px;top:1732px;width:54px;height:54px"></div>
<div class="dots" style="left:928px;top:1924px;width:42px;height:42px"></div>
<div class="photo" role="img" aria-label="Hands with stethoscope in front of a laptop showing a brain scan" style="left:574px;top:1792px;width:350px;height:311px;background:var(--ink)"></div>
<div class="photo" role="img" aria-label="Hands with stethoscope in front of a laptop showing a brain scan" style="left:579px;top:1796px;width:341px;height:303px;background:linear-gradient(160deg,#5c8fb8,#2b5a85 55%,#14304f)"></div>
<h3 class="service-name">Custom Software<br>Development</h3>
<div class="service-rule"></div>
<p class="service-text" style="top:1899px">Using carefully selected software tools and carefully designed custom applications can make running your business so much more enjoyable.</p>
<p class="service-text" style="top:1987px">Quillamber can provide an upfront quote and regular progress updates on your project to give you piece of mind.</p>

<h2 class="blog-title">Blog</h2>
<article class="post" style="left:75px">
  <div class="post-photo" role="img" aria-label="Hands using a tablet beside a stethoscope" style="background:linear-gradient(135deg,#e9eef2,#9aa8b4 60%,#3d4650)"></div>
  <div class="post-date">18<br>July</div>
  <h3 class="post-heading">Blog Title Heading 01</h3>
  <p class="post-excerpt">Lorem Ipsum simply dummy text the printingand ypesetting industry simply dummy Ipsum is dummy text of the printing...</p>
  <div class="post-arrow"><svg width="16" height="12" viewBox="0 0 16 12"><path d="M1 6h13M9 1l5 5-5 5" fill="none" stroke="#fff" stroke-width="2"/></svg></div>
</article>
<article class="post featured" style="left:432px">
  <div class="post-photo" role="img" aria-label="Scientist at a computer in a laboratory" style="background:linear-gradient(135deg,#dfe6ec,#8ea3b8 55%,#2e4a66)"></div>
  <div class="post-date">18<br>July</div>
  <h3 class="post-heading">Blog Title Heading 02</h3>
  <p class="post-excerpt">Lorem Ipsum simply dummy text the printingand ypesetting industry simply dummy Ipsum is dummy text of the printing...</p>
  <div class="post-arrow"><svg width="16" height="12" viewBox="0 0 16 12"><path d="M1 6h13M9 1l5 5-5 5" fill="none" stroke="#fff" stroke-width="2"/></svg></div>
</article>
<article class="post" style="left:790px">
  <div class="post-photo" role="img" aria-label="Doctor smiling at a laptop in her office" style="background:linear-gradient(135deg,#c9b79c,#e8e4dc 55%,#8b8f93)"></div>
  <div class="post-date">18<br>July</div>
  <h3 class="post-heading">Blog Title Heading 03</h3>
  <p class="post-excerpt">Lorem Ipsum simply dummy text the printingand ypesetting industry simply dummy Ipsum is dummy text of the printing....</p>
  <div class="post-arrow"><svg width="16" height="12" viewBox="0 0 16 12"><path d="M1 6h13M9 1l5 5-5 5" fill="none" stroke="#fff" stroke-width="2"/></svg></div>
</article>
<svg class="abs" style="left:710px;top:2806px" width="20" height="26" viewBox="0 0 20 26"><path d="M6 12V3a2 2 0 0 1 4 0v8l6 1c2 .4 3 2 2.6 4L17 23H7L2 16c-1-1.5 1-3 2.4-2z" fill="#fff" stroke="#222" stroke-width="1.2"/></svg>
<div class="btn btn-blue" style="left:523px;top:2859px;width:155px;height:37px">View More</div>

<h2 class="contact-title">Quick Contact</h2>
<div class="field" style="left:224px;top:3018px;width:243px;height:45px">Name*</div>
<div class="field" style="left:480px;top:3018px;width:243px;height:45px">Phone*</div>
<div class="field" style="left:735px;top:3018px;width:243px;height:45px">Email*</div>
<div class="field" style="left:224px;top:3078px;width:752px;height:170px">Message</div>
<div class="btn btn-blue" style="left:526px;top:3273px;width:155px;height:38px;font-size:12px">SEND</div>

<footer class="site-footer">
  <svg width="1200" height="430" viewBox="0 0 1200 430">
    <polygon points="0,144 1200,14 1200,430 0,430" fill="var(--ink)"/>
    <polygon points="0,138 1200,8 1200,14 0,144" fill="var(--white)"/>
    <polygon points="0,14 596,71 0,138" fill="var(--blue)"/>
  </svg>
</footer>
<div class="brand" style="left:75px;top:3572px;color:var(--white)"><span class="brand-dot" style="width:60px;height:60px;background:var(--white)"></span>Quillamber</div>

<div class="footer-head" style="left:428px">QUICK LINKS</div>
<div class="footer-rule" style="left:428px"></div>
<ul class="quick-links">
  <li>Home</li><li>About us</li><li>Our Services</li><li>Team</li><li>Contact us</li>
</ul>

<div class="footer-head" style="left:604px">CONTACT DETAIL</div>
<div class="footer-rule" style="left:604px"></div>
<div class="contact-line" style="top:3573px"><svg width="10" height="12" viewBox="0 0 10 12"><path d="M2 0l2 3-1 2c1 2 2 3 3 4l2-1 2 2-2 2C4 12 0 6 0 2z" fill="var(--blue)"/></svg>+61 400 555 012</div>
<div class="contact-line" style="top:3606px"><svg width="10" height="12" viewBox="0 0 10 12"><rect y="3" width="10" height="7" fill="var(--blue)"/><path d="M0 3l5 4 5-4" fill="none" stroke="var(--ink)"/></svg>mara@quillamber.com</div>
<div class="contact-line" style="top:3638px"><svg width="10" height="12" viewBox="0 0 10 12"><path d="M5 12C2 8 0 6 0 4a5 5 0 0 1 10 0c0 2-2 4-5 8z" fill="var(--blue)"/><circle cx="5" cy="4" r="1.8" fill="var(--ink)"/></svg><span>18 Harbour View Lane<br>Kingsford, Queensland, 4000<br>Australia</span></div>

<div class="footer-head" style="left:879px">NEWSLETTER</div>
<div class="footer-rule" style="left:879px"></div>
<div class="abs" style="left:879px;top:3571px;font-size:13px;color:var(--white)">Lorem Ipsum is simply dummy printing</div>
<div class="abs" style="left:879px;top:3596px;width:245px;height:32px;border-radius:16px;background:var(--white);font-size:12px;font-style:italic;color:var(--muted);padding:8px 20px">Email Address</div>
<div class="btn btn-blue" style="left:879px;top:3637px;width:245px;height:32px;font-size:12px">SUBSCRIBE</div>

<div class="bottom-bar"></div>
<p class="copyright">Copyright © 2022 <strong>QUILLAMBER</strong>, All Rights Reserved.</p>
<div class="social" style="left:953px;background:var(--blue)"></div>
<div class="social" style="left:1000px;background:var(--ink)"></div>
<div class="social" style="left:1046px;background:var(--ink)"></div>
<div class="social" style="left:1088px;background:var(--ink)"></div>

</body>
</html>
```